Brevik Seasoning
Brevik Seasoning - Food
Creative Brief
Simple
Tom Halvern
President and CEO
52190 Harlow Lane Sterling Heights, MI 48977
thalvern@brevikspice.com
Brevikspice.com
Xpert Xpert

```html
<!DOCTYPE html>
<html lang="en">
<head>
<meta charset="utf-8">
<title>Brevik Seasoning – Business Card</title>
<link rel="stylesheet" href="https://fonts.googleapis.com/css2?family=Open+Sans:wght@400;600&display=swap">
<style>
  :root{
    --stage:#d9d6d1;
    --card-black:#0b0b0b;
    --card-white:#fbfbfb;
    --ink:#2b2b2b;
    --ink-soft:#555;
    --accent-red:#c8332b;
    --accent-green:#7f9a2c;
    --accent-amber:#e1a62a;
    --rule:#9a9a9a;
  }
  *{margin:0;padding:0;box-sizing:border-box}
  html,body{width:1200px;height:904px;overflow:hidden}
  body{background:var(--stage);font-family:"Open Sans",Arial,sans-serif;position:relative}
  .card{position:absolute;left:240px;width:720px;height:400px;box-shadow:0 6px 18px rgba(0,0,0,.25);overflow:hidden}
  .card--front{top:32px;background:var(--card-black)}
  .card--back{top:472px;background:var(--card-white)}

  .brand{display:flex;align-items:center;gap:12px}
  .brand__mark{width:22px;height:22px;background:var(--accent-red)}
  .brand__name{font-weight:600;font-size:46px;letter-spacing:.5px;line-height:1}
  .card--front .brand{position:absolute;left:50%;top:50%;transform:translate(-50%,-50%)}
  .card--front .brand__name{color:#fff}
  .card--back .brand{position:absolute;left:58px;top:62px}
  .card--back .brand__name{color:var(--ink);font-size:40px}

  .person{position:absolute;right:48px;top:74px;text-align:right}
  .person__name{color:var(--accent-red);font-size:20px;font-weight:600}
  .person__title{color:var(--ink);font-size:15px;margin-top:2px}

  .divider{position:absolute;left:48px;right:48px;top:196px;border-top:2px dotted var(--rule)}

  .contact{position:absolute;left:58px;top:222px;color:var(--ink-soft);font-size:14px;line-height:22px}
  .contact__address{margin-bottom:4px}
  .contact__line{display:flex;align-items:center;gap:8px}
  .contact__line svg{width:13px;height:13px;flex:none}

  .footer-band{position:absolute;left:400px;right:0;bottom:26px;height:28px;background:var(--card-black)}
  .swatches{position:absolute;left:420px;bottom:20px;display:flex;gap:6px}
  .swatch{width:30px;height:40px}
  .swatch--red{background:var(--accent-red)}
  .swatch--green{background:var(--accent-green)}
  .swatch--amber{background:var(--accent-amber)}
  .web{position:absolute;right:22px;bottom:31px;color:#fff;font-size:15px}
</style>
</head>
<body>
  <section class="card card--front">
    <div class="brand">
      <span class="brand__mark"></span>
      <span class="brand__name">Brevik</span>
    </div>
  </section>

  <section class="card card--back">
    <div class="brand">
      <span class="brand__mark"></span>
      <span class="brand__name">Brevik</span>
    </div>

    <div class="person">
      <p class="person__name">Tom Halvern</p>
      <p class="person__title">President and CEO</p>
    </div>

    <div class="divider"></div>

    <div class="contact">
      <p class="contact__address">52190 Harlow Lane<br>Sterling Heights, MI 48977</p>
      <p class="contact__line">
        <svg viewBox="0 0 16 16" aria-hidden="true"><path fill="#6f9a3a" d="M3 2h3l1 3-2 1.5a9 9 0 0 0 4.5 4.5L11 9l3 1v3a1 1 0 0 1-1 1A12 12 0 0 1 2 3a1 1 0 0 1 1-1z"/></svg>
        586-555-0147
      </p>
      <p class="contact__line">
        <svg viewBox="0 0 16 16" aria-hidden="true"><rect x="4" y="1" width="8" height="14" rx="1.5" fill="none" stroke="#6f9a3a" stroke-width="1.5"/><circle cx="8" cy="12.5" r="1" fill="#6f9a3a"/></svg>
        248-555-0183
      </p>
      <p class="contact__line">
        <svg viewBox="0 0 16 16" aria-hidden="true"><rect x="1.5" y="3.5" width="13" height="9" fill="none" stroke="#6f9a3a" stroke-width="1.5"/><path d="M1.5 3.5 8 9l6.5-5.5" fill="none" stroke="#6f9a3a" stroke-width="1.5"/></svg>
        thalvern@brevikspice.com
      </p>
    </div>

    <div class="footer-band"></div>
    <div class="swatches">
      <span class="swatch swatch--red"></span>
      <span class="swatch swatch--green"></span>
      <span class="swatch swatch--amber"></span>
    </div>
    <p class="web">Brevikspice.com</p>
  </section>
</body>
</html>
```